依頼詳細
集合場所が分かりにくいので、周辺が混みあうときには2~3本立てて、その目印に使います。なるべく目立つ印象で、明るく楽しい感じが伝わってくるものが良いです。写真も添付しますのでご利用ください。
記載項目
記載項目:鳥取砂丘でパラグライダー体験!
サイズ:一般的なのぼりのサイズ(600×1800ミリ)
希望イメージ
シンプル 複雑
単色 カラフル
暗い 明るい
日常 高級
遊び心 厳粛
未来的 伝統的
女性的 男性的
希望する色
青、黄、オレンジ
納品ファイル
• 高解像度JPG (.jpg)
• イラストレーター形式 (.ai)
補足説明
当方のHPは、
http://hane.kumoba.info/
になります。
画像等は、参考にしていただければと思います。
■ 選んだ理由

今回かなり悩みました。
期間をじっくり置いて、いろいろな視点ですべての作品を見させていただいた中で、写真を大きくはっきり使っていただいたのと、その配置が絶妙で、文字の自由度が大きくなる点を評価しました。
写真の切り取り方が良かったと思います。

■ 提案者全員のお礼・コメント

多数のご提案まことにありがとうございました。
甲乙つけがたいものが多くて、自分がどうこう評価するにはおこがましい感覚を受けながらも、みなさまの作品をじっくり拝見して、吟味させていただきました。
写真以外の可能性も感じたり、キャラや文字を面白くデフォルメしてくださったり、斬新な構図を見せてくださったり、う~んと感心ばかりしていました。
当方、まったくデザインに関して素人にも関わらず、いろいろなことを勉強させていただいたように思います。
皆さまの貴重な時間を、このたびは本当にありがとうございました。m(_ _)m

```html
<!DOCTYPE html>
<html lang="ja">
<head>
<meta charset="UTF-8">
<title>鳥取砂丘でパラグライダー体験!</title>
<link rel="stylesheet" href="https://fonts.googleapis.com/css2?family=M+PLUS+Rounded+1c:wght@700;800;900&display=swap">
<style>
  :root {
    --sky-orange: #f39a1f;
    --cloud-white: #ffffff;
    --title-blue: #1d9ee6;
    --outline-yellow: #fff200;
    --accent-pink: #e6006e;
    --badge-pink: #ea4f86;
  }
  html, body {
    margin: 0;
    padding: 0;
    width: 1200px;
    height: 3600px;
    overflow: hidden;
    background: var(--sky-orange);
  }
  .banner {
    position: relative;
    width: 1200px;
    height: 3600px;
    overflow: hidden;
    background: var(--sky-orange);
  }
  .artwork {
    position: absolute;
    inset: 0;
    width: 1200px;
    height: 3600px;
    font-family: "M PLUS Rounded 1c", sans-serif;
  }
  .paraglider-illustration {
    position: absolute;
    left: 220px;
    top: 0;
    width: 780px;
    height: 800px;
    border-radius: 0 0 240px 240px;
    background: linear-gradient(180deg, #bfe6fb 0%, #ffffff 35%, #f6b9d3 75%, rgba(243,154,31,0) 100%);
  }
  .char { text-anchor: middle; dominant-baseline: central; }
  .tagline { font-size: 64px; font-weight: 800; fill: var(--cloud-white); }
  .title { font-size: 240px; font-weight: 900; }
  .title-outer { fill: var(--outline-yellow); stroke: var(--outline-yellow); stroke-width: 76px; stroke-linejoin: round; }
  .title-inner { fill: var(--cloud-white); stroke: var(--cloud-white); stroke-width: 36px; stroke-linejoin: round; }
  .title-fill { fill: var(--title-blue); }
  .headline {
    font-size: 150px; font-weight: 900; fill: var(--accent-pink);
    stroke: var(--cloud-white); stroke-width: 22px; stroke-linejoin: round; paint-order: stroke fill;
  }
  .badge-circle { fill: var(--badge-pink); stroke: var(--cloud-white); stroke-width: 8px; }
  .badge-text { font-size: 44px; font-weight: 800; fill: var(--cloud-white); text-anchor: middle; dominant-baseline: central; }
  .sparkle { fill: var(--cloud-white); }
</style>
</head>
<body>
<main class="banner">
  <div class="paraglider-illustration" role="img" aria-label="パラグライダーで空を飛ぶ女の子のイラスト(青白の縞模様の翼)"></div>

  <svg class="artwork" viewBox="0 0 1200 3600">
    <defs>
      <g id="title-chars" class="title">
        <text class="char" x="560" y="913">パ</text>
        <text class="char" x="560" y="1179">ラ</text>
        <text class="char" x="560" y="1445">グ</text>
        <text class="char" x="560" y="1711">ラ</text>
        <text class="char" x="560" y="1977">イ</text>
        <text class="char" x="560" y="2243">ダ</text>
        <text class="char" x="560" y="2509" transform="rotate(90 560 2509)">ー</text>
        <text class="char" x="560" y="2775">体</text>
        <text class="char" x="560" y="3041">験</text>
        <text class="char" x="560" y="3307">！</text>
      </g>
    </defs>

    <g class="clouds" fill="#ffffff" aria-hidden="true">
      <ellipse cx="1020" cy="170" rx="150" ry="70"/>
      <ellipse cx="1120" cy="130" rx="110" ry="85"/>
      <ellipse cx="60" cy="660" rx="150" ry="60"/>
      <ellipse cx="170" cy="690" rx="80" ry="40"/>
      <path d="M1200 1760 C1120 1740 1050 1790 1040 1860 C970 1840 900 1880 890 1950 C810 1940 750 2000 760 2070 C680 2070 620 2130 640 2200 C560 2200 500 2260 520 2330 C440 2340 390 2400 410 2470 C330 2470 280 2530 290 2600 C200 2600 140 2650 140 2720 C70 2720 20 2760 0 2800 L0 3600 L1200 3600 Z"/>
    </g>

    <g class="sparkles" aria-hidden="true">
      <path class="sparkle" d="M720 1960 L732 2000 L772 2012 L732 2024 L720 2064 L708 2024 L668 2012 L708 2000 Z"/>
      <path class="sparkle" d="M790 1840 L798 1864 L822 1872 L798 1880 L790 1904 L782 1880 L758 1872 L782 1864 Z"/>
    </g>

    <g class="tagline">
      <text class="char" x="312" y="875">雄</text>
      <text class="char" x="312" y="945">大</text>
      <text class="char" x="312" y="1015">な</text>
      <text class="char" x="312" y="1085">日</text>
      <text class="char" x="312" y="1155">本</text>
      <text class="char" x="312" y="1225">海</text>
      <text class="char" x="312" y="1295">を</text>
      <text class="char" x="312" y="1365">眺</text>
      <text class="char" x="312" y="1435">め</text>
      <text class="char" x="312" y="1505">な</text>
      <text class="char" x="312" y="1575">が</text>
      <text class="char" x="312" y="1645">ら</text>
      <text class="char" x="312" y="1715">空</text>
      <text class="char" x="312" y="1785">の</text>
      <text class="char" x="312" y="1855">散</text>
      <text class="char" x="312" y="1925">歩</text>
      <text class="char" x="312" y="1995">は</text>
      <text class="char" x="312" y="2065">気</text>
      <text class="char" x="312" y="2135">分</text>
      <text class="char" x="312" y="2205">爽</text>
      <text class="char" x="312" y="2275">快</text>
      <text class="char" x="312" y="2345">！</text>
    </g>

    <use href="#title-chars" class="title-outer" aria-hidden="true"/>
    <use href="#title-chars" class="title-inner" aria-hidden="true"/>
    <use href="#title-chars" class="title-fill"/>

    <g class="headline">
      <text class="char" x="1020" y="982">鳥</text>
      <text class="char" x="1020" y="1147">取</text>
      <text class="char" x="1020" y="1312">砂</text>
      <text class="char" x="1020" y="1477">丘</text>
      <text class="char" x="1020" y="1642">で</text>
      <text class="char" x="1020" y="1807">最</text>
      <text class="char" x="1020" y="1972">高</text>
      <text class="char" x="1020" y="2137">の</text>
      <text class="char" x="1020" y="2302">思</text>
      <text class="char" x="1020" y="2467">い</text>
      <text class="char" x="1020" y="2632">出</text>
      <text class="char" x="1020" y="2797">！</text>
    </g>

    <g class="badge">
      <circle class="badge-circle" cx="960" cy="3352" r="180"/>
      <text class="badge-text" x="960" y="3290">お子様も</text>
      <text class="badge-text" x="960" y="3352">安心して</text>
      <text class="badge-text" x="960" y="3414">体験できる</text>
    </g>
  </svg>
</main>
</body>
</html>
```